Shift Haven Brochure for on call home care staffing

Brochure to describe Shift haven services. Shift haven provides after hours on-call staffing and scheduling only for home care agencies. We are 100% US Based with real agents in person answering calls. We act as an extension of their agency and integrate seamlessly. I dropped in my attempt at the brochure but my AI images suck. We want realistic images with an Americana feel. I also don't want the gold color or the same images on the new one. Feel free to redo the writing.

Target Market(s)

home care agencies

Industry/Entity Type

Health care staffing

Font styles to use
Serif
Sans Serif

Colors
0054AA
0677BA
7BADD7
CADEEF
E8F1F8

Requirements
Must have
• Catchy headlines
Nice to have
• I'd like to see professional style brochure with squares integrated in.
Should not have
• VIBRANT COLORS

```html
<!DOCTYPE html>
<html lang="en">
<head>
<meta charset="utf-8">
<title>Shift Haven Brochure</title>
<link href="https://fonts.googleapis.com/css2?family=Montserrat:wght@400;500;600;700;800&family=Merriweather:wght@400&display=swap" rel="stylesheet">
<style>
:root{
  --bg:#e9eaec;
  --navy:#0d2b4d;
  --ink:#1f2833;
  --blue:#0054AA;
  --blue-mid:#0677BA;
  --blue-soft:#7BADD7;
  --blue-pale:#CADEEF;
  --blue-mist:#E8F1F8;
  --red:#a21d35;
  --grey:#f1f2f4;
  --white:#ffffff;
  --sans:'Montserrat',Arial,sans-serif;
  --serif:'Merriweather',Georgia,serif;
}
*{box-sizing:border-box;margin:0;padding:0}
html,body{width:1200px;height:935px;overflow:hidden;background:var(--bg);font-family:var(--sans);color:var(--ink)}
.stage{position:relative;width:1200px;height:935px;background:linear-gradient(180deg,#f1f2f4,#dfe1e4)}
.sheet{position:absolute;left:66px;width:1066px;height:355px;background:var(--white);box-shadow:0 3px 10px rgba(0,0,0,.18);overflow:hidden}
.sheet--outside{top:90px}
.sheet--inside{top:503px}
.panel{position:absolute;top:0;width:356px;height:355px;overflow:hidden}
.panel--1{left:0}.panel--2{left:355px}.panel--3{left:710px}
.abs{position:absolute}
.photo{position:absolute}
.brand{position:absolute;display:flex;align-items:center;justify-content:center;gap:7px}
.brand__square{width:11px;height:11px;background:var(--blue);flex:none}
.brand__name{font-weight:700;font-size:13px;letter-spacing:.5px;color:var(--blue)}
.rule{height:2px;background:var(--red)}
.center{text-align:center}

/* outside panel 1 */
.diff__head{left:0;top:0;width:356px;height:84px;background:linear-gradient(90deg,#1c2734 0%,#14345a 60%,#0b4f93 100%);text-align:center;padding-top:18px}
.diff__title{color:#fff;font-weight:700;font-size:17px;letter-spacing:.3px}
.diff__head .rule{width:280px;margin:5px auto 6px}
.diff__sub{font-family:var(--serif);color:var(--blue-soft);font-size:12px}
.diff__body{left:0;top:84px;width:356px;height:271px;background:linear-gradient(180deg,#fff 0%,#f6f9fc 60%,var(--blue-pale) 100%)}
.diff__grid{left:107px;top:113px;width:140px;height:140px;border:1px solid #d98a9a;padding:10px;display:grid;grid-template-columns:1fr 1fr;gap:7px}
.tile{display:flex;align-items:center;justify-content:center}
.tile--navy{background:var(--navy)}.tile--blue{background:var(--blue-mid)}.tile--red{background:var(--red)}
.label{font-size:10px;line-height:1.2;color:var(--ink)}
.diff__rule{left:22px;top:265px;width:312px;height:1px;background:var(--blue-mid)}
.diff__copy{left:22px;top:280px;width:312px;font-size:8.4px;line-height:1.35;text-align:justify;color:var(--ink)}

/* outside panel 2 */
.extend__band{left:0;top:84px;width:356px;height:95px;background:var(--ink);text-align:center;padding-top:18px}
.extend__title{color:#fff;font-weight:700;font-size:17px;letter-spacing:.3px}
.extend__lead{font-family:var(--serif);color:var(--blue-mid);font-size:12px;line-height:1.3;margin-top:4px}
.extend__band .rule{width:82px;margin:4px auto 0;height:1.5px}
.contact{left:178px;top:179px;width:178px;height:176px;background:var(--grey);padding:20px 18px}
.contact__card{border:1px solid #b9bcc2;background:#fff;height:134px;padding:6px 8px;text-align:center}
.contact__tag{background:var(--red);color:#fff;font-size:11px;font-weight:500;padding:3px 0}
.ico-sq{width:14px;height:14px;background:var(--ink);margin:8px auto 3px;display:flex;align-items:center;justify-content:center}
.contact__phone{font-weight:700;font-size:16px;color:var(--ink)}
.contact__city{font-size:7.5px;color:#555}
.contact__mail{font-size:7.5px;color:#555;line-height:1.25}

/* outside panel 3 */
.trust__box{left:0;top:84px;width:258px;height:271px;background:linear-gradient(180deg,#1f2a36 0%,#163a63 45%,#0f5ca8 100%)}
.trust__title{left:0;top:33px;width:258px;color:#fff;font-weight:600;font-size:18px;line-height:1.3;text-align:center;letter-spacing:.4px}
.trust__box .rule{position:absolute;left:70px;top:108px;width:118px;height:1.5px}
.trust__sub{left:0;top:118px;width:258px;font-family:var(--serif);color:var(--blue-soft);font-size:12px;line-height:1.35;text-align:center}
.trust__cta{left:0;top:327px;width:258px;height:28px;background:var(--red);color:#fff;font-size:13px;font-weight:500;text-align:center;line-height:28px}

/* inside panel 1 */
.why__box{left:23px;top:18px;width:140px;height:140px;border:1px solid #9aa3ad;text-align:center;padding-top:30px}
.why__title{font-weight:700;font-size:12.5px;line-height:1.25;color:var(--navy)}
.why__box .brand{position:static;margin-top:26px}
.why__item{position:absolute;left:195px;display:flex;align-items:center;gap:16px}
.why__icon{width:56px;height:56px;display:flex;align-items:center;justify-content:center;flex:none}
.why__icon--navy{background:var(--navy)}.why__icon--grey{background:var(--grey)}
.why__text{font-size:10px;line-height:1.25;color:var(--ink)}
.why__line{position:absolute;left:195px;width:160px;height:1px;background:var(--blue-mid)}

/* inside panel 2 */
.services__title{left:15px;top:17px;width:328px;height:56px;border:1.5px solid var(--navy);text-align:center;line-height:53px;font-weight:700;font-size:30px;letter-spacing:9px;color:var(--navy)}
.services__title span{color:var(--blue-mid)}
.services__banner{left:0;top:88px;width:356px;height:90px;background:linear-gradient(90deg,#6aa4d6 0%,#a9cbea 55%,#dfe9f4 75%,#b9c9da 100%)}
.services__quote{left:22px;top:118px;font-family:var(--serif);color:#fff;font-size:12px;line-height:1.45}
.services__area{left:0;top:178px;width:356px;height:177px;background:linear-gradient(135deg,var(--blue-mist),#fff 50%,var(--blue-pale))}
.services__photo-frame{left:26px;top:200px;width:140px;height:140px;border:1px solid #b9bcc2;background:#fff;padding:10px}
.services__card{left:180px;top:200px;width:162px;height:140px;border:1px solid #b9bcc2;background:#fff;text-align:center;padding:12px 8px 0}
.svc__name{font-weight:700;font-size:11px;color:var(--navy)}
.svc__note{font-size:6.8px;color:#333;line-height:1.2}
.svc__sep{height:1px;background:var(--red);margin:6px 4px 8px}

/* inside panel 3 */
.answer__box{left:0;top:0;width:176px;height:178px;background:linear-gradient(180deg,#1c2734,#163b66)}
.answer__title{left:0;top:84px;width:176px;text-align:center;color:#fff;font-weight:600;font-size:18px;line-height:1.3;letter-spacing:.4px}
.answer__title .rule{width:116px;height:1.5px;margin:2px auto 4px}
.answer__copy{left:28px;top:200px;width:300px;font-size:9.5px;line-height:1.35;text-align:center;color:var(--ink)}
.answer__band{left:0;top:271px;width:356px;height:84px;background:var(--blue-mid)}
.chip{position:absolute;top:286px;width:57px;height:57px;border:1px solid rgba(255,255,255,.8);color:#fff;font-size:6.5px;font-weight:500;text-align:center;display:flex;flex-direction:column;align-items:center;justify-content:center;gap:3px;line-height:1.15}
</style>
</head>
<body>
<main class="stage">

  <section class="sheet sheet--outside">

    <div class="panel panel--1">
      <header class="abs diff__head">
        <h2 class="diff__title">THE SHIFTHAVEN DIFFERENCE</h2>
        <div class="rule"></div>
        <p class="diff__sub">Real People. Real Support. Real Results</p>
      </header>
      <div class="abs diff__body" role="img" aria-label="Faint map of the United States on a soft blue background"></div>
      <p class="abs label center" style="left:28px;top:134px;width:80px">HIPAA<br>Compliant<br>Processes</p>
      <p class="abs label" style="left:262px;top:134px;width:80px">Integrated<br>With Your<br>Software</p>
      <p class="abs label center" style="left:28px;top:204px;width:80px">Reduce<br>Burnout for<br>Your Team</p>
      <p class="abs label" style="left:262px;top:210px;width:80px">Trusted<br>Nationwide</p>
      <div class="abs diff__grid">
        <div class="tile tile--navy"><svg width="30" height="30" viewBox="0 0 30 30"><path d="M15 3v24M10 8h10M9 12c4 2 8 2 12 0M9 18c4-2 8-2 12 0" stroke="#fff" stroke-width="2" fill="none"/></svg></div>
        <div class="tile tile--blue"><svg width="30" height="30" viewBox="0 0 30 30"><rect x="4" y="10" width="20" height="14" fill="none" stroke="#fff" stroke-width="2"/><path d="M4 14h20" stroke="#fff" stroke-width="2"/><circle cx="23" cy="9" r="4" fill="none" stroke="#fff" stroke-width="2"/></svg></div>
        <div class="tile tile--red"><svg width="34" height="26" viewBox="0 0 34 26"><circle cx="9" cy="8" r="3.5" fill="#fff"/><circle cx="17" cy="7" r="4" fill="#fff"/><circle cx="25" cy="8" r="3.5" fill="#fff"/><path d="M3 22v-6c0-3 3-4 6-4s4 1 4 1v9zM12 22v-7c0-3 2-4 5-4s5 1 5 4v7zM21 22v-9s1-1 4-1 6 1 6 4v6z" fill="#fff"/></svg></div>
        <div class="tile tile--navy"><svg width="30" height="30" viewBox="0 0 30 30"><circle cx="15" cy="15" r="13" fill="#fff"/><circle cx="15" cy="15" r="11" fill="#c83a48"/><path d="M4 11h22M4 15h22M4 19h22M5 23h20" stroke="#fff" stroke-width="1.6"/><path d="M5 8a11 11 0 0 1 10-4v11H4z" fill="#1d3f7a"/></svg></div>
      </div>
      <div class="abs diff__rule"></div>
      <p class="abs diff__copy">ShiftHaven provides reliable on-call staffing designed for home care. Our U.S.-based team ensures every shift is covered with qualified, compassionate caregivers—so you can focus on care while we handle the scheduling. From last-minute coverage to ongoing support, we help you stay efficient, stress-free, and maintain the high standards your clients deserve.</p>
    </div>

    <div class="panel panel--2">
      <div class="brand" style="left:0;width:356px;top:36px">
        <span class="brand__square"></span><span class="brand__name">SHIFT HAVEN</span>
      </div>
      <div class="abs extend__band">
        <h2 class="extend__title">LET’S EXTEND YOUR TEAM</h2>
        <p class="extend__lead">Ready for stress-free after-hours coverage?<br>Call us today.</p>
        <div class="rule"></div>
      </div>
      <div class="photo" style="left:0;top:179px;width:178px;height:176px;background:linear-gradient(135deg,#e4e6e8,#b7c4d2 60%,#8aa4c0)" role="img" aria-label="Caregiver in blue scrubs sitting with a smiling senior man at home"></div>
      <div class="abs contact">
        <div class="contact__card">
          <div class="contact__tag">24/7 SERVICES</div>
          <div class="ico-sq"><svg width="9" height="9" viewBox="0 0 10 10"><path d="M2 1l2 2-1 1.5c.5 1 1.5 2 2.5 2.5L7 6l2 2-1.5 1.5C5 9 1 5 .5 2.5z" fill="#fff"/></svg></div>
          <div class="contact__phone">555.014.2290</div>
          <div class="contact__city">Maple Ridge Texas</div>
          <div class="ico-sq"><svg width="9" height="7" viewBox="0 0 10 8"><rect x=".5" y=".5" width="9" height="7" fill="none" stroke="#fff"/><path d="M.5.5L5 4.5 9.5.5" stroke="#fff" fill="none"/></svg></div>
          <div class="contact__mail">jordan@<br>shifthavencare.com</div>
        </div>
      </div>
    </div>

    <div class="panel panel--3">
      <div class="photo" style="left:0;top:0;width:356px;height:84px;background:linear-gradient(90deg,#fff 35%,#d7e6f4 80%,var(--blue-soft))" role="img" aria-label="Faint pattern of small squares fading into light blue"></div>
      <div class="brand" style="left:0;width:258px;top:36px">
        <span class="brand__square"></span><span class="brand__name">SHIFT HAVEN</span>
      </div>
      <div class="photo" style="left:0;top:84px;width:356px;height:271px;background:linear-gradient(180deg,#d6e3ef,#b9cde1 55%,#dfe6ee)" role="img" aria-label="Smiling call agent with a headset, arms crossed, beside a waving American flag"></div>
      <div class="abs trust__box">
        <h2 class="abs trust__title">ON-CALL<br>HOME CARE STAFFING<br>YOU CAN TRUST</h2>
        <div class="rule"></div>
        <p class="abs trust__sub">100% U.S. Based<br>Real Agents, Real Support</p>
        <div class="photo" style="left:0;top:190px;width:258px;height:53px;background:linear-gradient(90deg,#243b5c,#8e9fb4 50%,#c9d2dc)" role="img" aria-label="American flag stars and stripes"></div>
      </div>
      <div class="abs trust__cta">Get Your Weekends Back</div>
    </div>
  </section>

  <section class="sheet sheet--inside">

    <div class="panel panel--1">
      <div class="abs why__box">
        <h3 class="why__title">WHY AGENCIES<br>TRUST</h3>
        <div class="brand"><span class="brand__square"></span><span class="brand__name">SHIFT HAVEN</span></div>
      </div>
      <div class="photo" style="left:0;top:178px;width:178px;height:177px;background:linear-gradient(135deg,#eef1f4,#c4d3e2 55%,#8aa6c4)" role="img" aria-label="Cheerful call agent with headset giving a thumbs up at a laptop"></div>
      <div class="why__item" style="top:18px">
        <div class="why__icon why__icon--navy"><svg width="32" height="32" viewBox="0 0 30 30"><circle cx="15" cy="15" r="13" fill="#fff"/><circle cx="15" cy="15" r="11" fill="#c83a48"/><path d="M4 11h22M4 15h22M4 19h22M5 23h20" stroke="#fff" stroke-width="1.6"/><path d="M5 8a11 11 0 0 1 10-4v11H4z" fill="#1d3f7a"/></svg></div>
        <p class="why__text">100%<br>U.S. Based</p>
      </div>
      <div class="why__line" style="top:89px"></div>
      <div class="why__item" style="top:109px">
        <div class="why__icon why__icon--grey"><svg width="32" height="30" viewBox="0 0 32 30"><path d="M10 12l8-7 8 7v8H10z" fill="var(--navy)"/><rect x="16" y="15" width="4" height="5" fill="#fff"/><path d="M2 22h7l5 3h8l6-4v3l-7 5H2z" fill="var(--navy)"/></svg></div>
        <p class="why__text">Experts in<br>Home Care</p>
      </div>
      <div class="why__line" style="top:185px"></div>
      <div class="why__item" style="top:206px">
        <div class="why__icon why__icon--navy"><svg width="34" height="34" viewBox="0 0 34 34"><circle cx="17" cy="17" r="14" fill="none" stroke="#fff" stroke-width="2" stroke-dasharray="3 2"/><text x="17" y="19" font-family="Montserrat,sans-serif" font-weight="700" font-size="11" fill="#fff" text-anchor="middle">24</text><text x="17" y="25" font-family="Montserrat,sans-serif" font-size="4" fill="#fff" text-anchor="middle">HOURS</text></svg></div>
        <p class="why__text">Seamless<br>After-Hours<br>Coverage</p>
      </div>
      <div class="why__line" style="top:275px"></div>
      <div class="why__item" style="top:287px">
        <div class="why__icon why__icon--grey"><svg width="32" height="30" viewBox="0 0 32 30"><path d="M19 14c-3-2-7-5-7-8a3.5 3.5 0 0 1 7-1 3.5 3.5 0 0 1 7 1c0 3-4 6-7 8z" fill="var(--navy)"/><path d="M2 20h7l5 3h8l6-4v3l-7 5H2z" fill="var(--navy)"/></svg></div>
        <p class="why__text">Compassionate<br>Support</p>
      </div>
    </div>

    <div class="panel panel--2">
      <h2 class="abs services__title">SERVI<span>CES</span></h2>
      <div class="abs services__banner" role="img" aria-label="Sunlit sky with an American flag on the right"></div>
      <p class="abs services__quote">We don’t just take calls.<br>We keep your agency moving.</p>
      <div class="abs services__area"></div>
      <div class="abs services__photo-frame">
        <div style="width:100%;height:100%;background:linear-gradient(135deg,#f2f3f5,#d9c3b4 55%,#9eb6cf)" role="img" aria-label="Caregiver holding an elderly person's hands"></div>
      </div>
      <div class="abs services__card">
        <div class="svc__name">ON-CALL STAFFING</div>
        <div class="svc__note">“We answer as your agency.”</div>
        <div class="svc__sep"></div>
        <div class="svc__name">SCHEDULING</div>
        <div class="svc__note">Real-time shift coverage<br>and updates.</div>
        <div class="svc__sep"></div>
        <div class="svc__name">INTAKE</div>
        <div class="svc__note">Never miss a client opportunity.</div>
      </div>
    </div>

    <div class="panel panel--3">
      <div class="abs answer__box">
        <svg class="abs" style="left:68px;top:22px" width="40" height="40" viewBox="0 0 34 34"><circle cx="17" cy="17" r="15" fill="none" stroke="#fff" stroke-width="1.6"/><path d="M17 3v3M17 28v3M3 17h3M28 17h3" stroke="#fff" stroke-width="1.6"/><text x="17" y="19" font-family="Montserrat,sans-serif" font-weight="700" font-size="11" fill="#fff" text-anchor="middle">24</text><text x="17" y="24.5" font-family="Montserrat,sans-serif" font-size="4" fill="#fff" text-anchor="middle">HOURS</text></svg>
        <h2 class="abs answer__title">WE ANSWER<div class="rule"></div>WHEN<br>YOU CAN’T</h2>
      </div>
      <div class="photo" style="left:176px;top:0;width:180px;height:178px;background:linear-gradient(135deg,#2a4466,#6f8fb3 55%,#c7d3df)" role="img" aria-label="Call center agents with headsets working at computers"></div>
      <p class="abs answer__copy">At Shifthaven, we extend your agency after hours with live, U.S.-based agents who handle calls, scheduling, and urgent staffing. Your clients are never left waiting — and your staff can truly rest.</p>
      <div class="abs answer__band"></div>
      <div class="chip" style="left:42px">
        <svg width="16" height="16" viewBox="0 0 10 10"><path d="M2 1l2 2-1 1.5c.5 1 1.5 2 2.5 2.5L7 6l2 2-1.5 1.5C5 9 1 5 .5 2.5z" fill="none" stroke="#fff" stroke-width=".8"/></svg>
        <span>CALL<br>HANDLING</span>
      </div>
      <div class="chip" style="left:150px">
        <svg width="16" height="16" viewBox="0 0 16 16"><rect x="1.5" y="3" width="13" height="11.5" fill="none" stroke="#fff" stroke-width="1.2"/><path d="M1.5 6.5h13M5 1v3M11 1v3M4 9h2M7 9h2M10 9h2M4 12h2M7 12h2" stroke="#fff" stroke-width="1.2"/></svg>
        <span>SCHEDULE<br>-ING</span>
      </div>
      <div class="chip" style="left:258px">
        <svg width="18" height="18" viewBox="0 0 34 34"><circle cx="17" cy="17" r="15" fill="none" stroke="#fff" stroke-width="2"/><text x="17" y="20" font-family="Montserrat,sans-serif" font-weight="700" font-size="12" fill="#fff" text-anchor="middle">24</text></svg>
        <span>ON CALL<br>COVERAGE</span>
      </div>
    </div>
  </section>

</main>
</body>
</html>
```